Brochures for Sheds and Cabins

We require a brochure design for our cabin. We currently have an outdated brochure but this doesn't suit our website style. We want something more modern to match our website www.kelvoyards.co.nz. The specifications for this model is on our website link https://kelvoyards.co.nz/collections/premier-cabins-studios/products/classic-studio. The purpose of the brochure is to sell the cabin to the client making them desirable. We need the same contact information as the old brochure but we need it to be redesigned with a modern look. Ideal aspects we need it to feature is product prices, name, product info, images, and finance available, bespoke sheds and cabins, tailor made.

Target Market(s)

Home owners, Parents with Teenagers, Working from home people. Self Employed.

Colors

Designer to choose colors to be used in the design.

Requirements
Must have
• Must have modern look which matches website.
• Clear specifications on the product
• Creative Design

```html
<!DOCTYPE html>
<html lang="en">
<head>
<meta charset="utf-8">
<title>Coastal Foldview Studio – Kelvo Yards Ltd</title>
<link href="https://fonts.googleapis.com/css2?family=Raleway:wght@300;400;500&family=Mulish:wght@400;600;700&display=swap" rel="stylesheet">
<style>
  :root {
    --brand-blue: #1d84c6;
    --brand-navy: #1c5f94;
    --ink: #2a2a2a;
    --ink-soft: #4a4a4a;
    --rule: #3d95cf;
    --paper: #ffffff;
  }
  * { box-sizing: border-box; margin: 0; padding: 0; }
  html, body { width: 848px; height: 1200px; overflow: hidden; background: var(--paper); }
  body { font-family: "Mulish", Arial, sans-serif; color: var(--ink); }
  .brochure { position: relative; width: 848px; height: 1200px; overflow: hidden; background: var(--paper); }

  .hero-photo {
    position: absolute; left: 0; top: 0; width: 848px; height: 712px;
    background: linear-gradient(160deg, #cfd9e2 0%, #8fa27c 28%, #3a3c3f 45%, #2e2f31 70%, #b48a5a 86%, #6f8d4a 100%);
  }

  .title-panel {
    position: absolute; left: 475px; top: 0; width: 333px; height: 242px;
    background: var(--brand-blue); color: var(--paper);
    padding: 34px 0 0 26px;
  }
  .title-panel .model-line,
  .title-panel .model-name { font-family: "Raleway", Arial, sans-serif; font-size: 34px; line-height: 1.08; white-space: nowrap; }
  .title-panel .model-line { font-weight: 300; }
  .title-panel .model-name { font-weight: 400; }
  .title-panel .title-rule { margin-top: 10px; width: 307px; height: 2px; background: var(--paper); }
  .price { position: absolute; left: 24px; top: 134px; font-weight: 700; display: flex; align-items: flex-start; }
  .price .currency { font-size: 46px; line-height: 1; margin-top: 14px; }
  .price .whole { font-size: 88px; line-height: 0.82; letter-spacing: -3px; }
  .price .stack { display: flex; flex-direction: column; margin-left: 2px; }
  .price .cents { font-size: 50px; line-height: 0.9; letter-spacing: -1px; }
  .price .tax { font-family: "Raleway", Arial, sans-serif; font-weight: 400; font-size: 20px; line-height: 1; margin-left: 6px; }

  .pitch-panel {
    position: absolute; left: 450px; top: 577px; width: 358px; height: 278px;
    background: var(--brand-blue); color: var(--paper);
    padding: 12px 14px 0 22px;
  }
  .pitch-panel h2 { font-family: "Raleway", Arial, sans-serif; font-weight: 400; font-size: 42px; line-height: 1.06; }
  .pitch-panel h2 span { display: block; white-space: nowrap; }
  .pitch-panel p { font-size: 10.6px; line-height: 1.38; margin-top: 10px; }
  .pitch-panel p + p { margin-top: 9px; }

  .feature-grid {
    position: absolute; left: 78px; top: 746px; width: 300px; list-style: none;
    display: grid; grid-template-columns: 162px 138px; row-gap: 22px;
  }
  .feature { display: flex; align-items: center; gap: 9px; font-size: 14px; line-height: 1.05; text-transform: uppercase; color: var(--ink-soft); }
  .feature svg { flex: none; }

  .spec-heading {
    position: absolute; left: 40px; top: 868px; width: 768px;
    display: flex; align-items: center; gap: 10px;
  }
  .spec-heading .line { flex: 1; height: 1px; background: var(--rule); }
  .spec-heading h3 { font-family: "Raleway", Arial, sans-serif; font-weight: 400; font-size: 35px; color: var(--ink); line-height: 1; }

  .spec-columns { position: absolute; left: 40px; top: 921px; width: 768px; height: 156px; display: flex; }
  .spec-col { font-size: 13.5px; line-height: 1.36; color: var(--ink-soft); }
  .spec-col:nth-child(1) { width: 252px; padding-right: 10px; }
  .spec-col:nth-child(2) { width: 244px; padding-left: 10px; border-left: 1.5px solid var(--rule); }
  .spec-col:nth-child(3) { width: 272px; padding-left: 10px; border-left: 1.5px solid var(--rule); margin-left: 10px; }
  .spec-col .key { color: var(--ink); font-weight: 600; }

  .company-name { position: absolute; left: 40px; top: 1112px; display: flex; align-items: center; gap: 10px; }
  .company-name .square { width: 18px; height: 18px; background: var(--brand-blue); }
  .company-name .name { font-weight: 700; font-size: 22px; color: var(--brand-blue); white-space: nowrap; }

  .contact { position: absolute; left: 320px; top: 1118px; font-size: 13.2px; line-height: 1.4; color: var(--ink); font-style: normal; white-space: nowrap; }
</style>
</head>
<body>
<main class="brochure">
  <div class="hero-photo" role="img" aria-label="Photo of a dark-clad garden studio with white bifold glass doors, an awning window and a timber deck on a lawn, hedge behind"></div>

  <header class="title-panel">
    <div class="model-line">Coastal</div>
    <div class="model-name">Foldview Studio</div>
    <div class="title-rule"></div>
    <div class="price">
      <span class="currency">$</span><span class="whole">15</span>
      <span class="stack"><span class="cents">,700</span><span class="tax">incl.GST</span></span>
    </div>
  </header>

  <section class="pitch-panel">
    <h2><span>The perfect</span><span>addition to</span><span>your back yard!</span></h2>
    <p>Our point of difference is making your ideas and style come to life with our expert Sales team and experienced builders. We listen to your ideas, we care about you, your home and your personal taste. Creating, designing and manufacturing building spaces just as you would like them is our specialty.</p>
    <p>We have a Signature range of sheds and cabins that can be purchased as is or customized to your needs.</p>
  </section>

  <ul class="feature-grid">
    <li class="feature"><svg width="28" height="28" viewBox="0 0 28 28"><circle cx="14" cy="14" r="12" fill="none" stroke="var(--brand-navy)" stroke-width="2.4"/><path d="M8 14l5 5 11-13" fill="none" stroke="var(--brand-navy)" stroke-width="2.6" stroke-linecap="round"/></svg><span>Top quality<br>products</span></li>
    <li class="feature"><svg width="28" height="28" viewBox="0 0 28 28"><circle cx="14" cy="14" r="12" fill="none" stroke="var(--brand-navy)" stroke-width="2.4"/><path d="M8 14l5 5 11-13" fill="none" stroke="var(--brand-navy)" stroke-width="2.6" stroke-linecap="round"/></svg><span>Reliable<br>delivery</span></li>
    <li class="feature"><svg width="28" height="28" viewBox="0 0 28 28"><circle cx="14" cy="14" r="12" fill="none" stroke="var(--brand-navy)" stroke-width="2.4"/><path d="M8 14l5 5 11-13" fill="none" stroke="var(--brand-navy)" stroke-width="2.6" stroke-linecap="round"/></svg><span>Sizes under<br>10sqm</span></li>
    <li class="feature"><svg width="28" height="28" viewBox="0 0 28 28"><circle cx="14" cy="14" r="12" fill="none" stroke="var(--brand-navy)" stroke-width="2.4"/><path d="M8 14l5 5 11-13" fill="none" stroke="var(--brand-navy)" stroke-width="2.6" stroke-linecap="round"/></svg><span>Custom<br>designs</span></li>
  </ul>

  <div class="spec-heading"><span class="line"></span><h3>Especifications</h3><span class="line"></span></div>

  <section class="spec-columns">
    <div class="spec-col">
      <div class="key">Size 2.4m x 4m x 2.4m</div>
      <div>NZ H3.2 Treated Pine - Exterior Cladding (Unpainted)</div>
      <div class="key">75 x 50 Dressed Pine Framing</div>
      <div>1 x Aluminium 3-Fold Bifold Door - 2100mm x 2000mm</div>
      <div class="key">1 x Aluminium Single Awning Window - 700mm x 700mm</div>
    </div>
    <div class="spec-col">
      <div>1 x Aluminium Large Awning Window - 1000mmx 1200mm</div>
      <div class="key">Corrugated Colored Steel Roofing and Flashings</div>
      <div>Aluminium Joinery Powder Coat Color</div>
      <div class="key">Single Glazed Glass</div>
      <div>Overhang - 600mm</div>
    </div>
    <div class="spec-col">
      <div class="key">Deck - 1000mm</div>
      <div>Plywood Floor - 19mm</div>
      <div class="key">Joists</div>
      <div>Bearers</div>
      <div class="key">Lined with Building paper</div>
      <div class="key">Interior Lined with V Groove</div>
      <div>Plywood (Untreated), Insulation in Walls and Roof with Pre-Electrical Wiring</div>
    </div>
  </section>

  <footer>
    <div class="company-name"><span class="square"></span><span class="name">Kelvo Yards Ltd</span></div>
    <address class="contact">
      KELVO YARDS LTD &nbsp;|&nbsp; 48 HALDEN RD, WIRI, AUCKLAND &nbsp;|&nbsp; PH: 0800 555 019<br>
      sales@kelvoyards.co.nz &nbsp;|&nbsp; www.kelvoyards.co.nz
    </address>
  </footer>
</main>
</body>
</html>
```